依頼詳細
平成26年     開業しましたが、平成27年1月より院の認知度アップ、新規患者様獲得の為
合計で2万枚程度を複数回に分けて新聞折込チラシを行います。
A4サイズでのチラシデザイン制作をお願いいたします。
現在制作中のホームページへの誘導を促したいのでURL入力のスペース確保や、『鈴風台接骨院で検索』などの記載をお願いします。
URLは12月12日現在決定していない為、仮のURLでのデザイン作成をお願いいたします。

シンプルながらも手に取った方の印象に残るような折込チラシデザインをお願いいたします。
記載項目
添付資料内のロゴ・HPサンプル等をご参照いただき、院名/住所/連絡先/受付時間/地図等の記載をお願いいたします。
サイズ
A4
ページ数
片面
希望イメージ
シンプル 複雑
単色 カラフル
暗い 明るい
日常 高級
遊び心 厳粛
未来的 伝統的
女性的 男性的
希望する色
納品ファイル
• 高解像度JPG (.jpg)
• イラストレーター形式 (.ai)
補足説明
ホームページURLはわかり次第ご連絡いたします。

この度はご提案いただきまして誠にありがとうございます。
納品までスムーズにご対応いただき、感謝いたします。
またの機会がございましたらよろしくお願いいたします。

納品までスムーズにご対応いただき、感謝いたします。

短い期間にもかかわらずたくさんのご提案いただき驚いております。

```html
<!DOCTYPE html>
<html lang="ja">
<head>
<meta charset="utf-8">
<title>鈴風台接骨院 チラシ</title>
<link href="https://fonts.googleapis.com/css2?family=Noto+Sans+JP:wght@400;500;700;900&family=Shippori+Mincho:wght@700;800&display=swap" rel="stylesheet">
<style>
:root{
  --teal:#1e98a8;
  --teal-dark:#147885;
  --green:#8cc43c;
  --green-light:#dcefc0;
  --orange:#f29a2e;
  --pink:#ee8aa2;
  --ink:#333;
  --muted:#666;
  --paper:#fff;
  --mist:#eef6f3;
}
*{margin:0;padding:0;box-sizing:border-box}
html,body{width:851px;height:1200px;overflow:hidden;background:#fff}
body{font-family:"Noto Sans JP",sans-serif;color:var(--ink)}
.flyer{position:relative;width:851px;height:1200px;background:var(--paper);overflow:hidden}
.abs{position:absolute}

.tagline{left:0;right:0;top:22px;text-align:center;font-size:14px;letter-spacing:.3em;color:var(--teal-dark);font-family:"Shippori Mincho",serif}
.clinic-name{left:0;right:0;top:40px;text-align:center;font-family:"Shippori Mincho",serif;font-weight:800;font-size:64px;letter-spacing:.12em;color:var(--teal)}
.title-rule{left:40px;right:40px;top:122px;height:4px;background:linear-gradient(90deg,transparent,var(--teal),transparent)}

.hero{left:0;right:0;top:138px;height:222px;background:linear-gradient(90deg,#f3ece6 0%,#f3ece6 50%,#eef2f5 50%,#e4eaef 100%)}
.hero-photo-left{left:0;top:0;width:420px;height:222px;background:linear-gradient(135deg,#e9dfd5,#cfd9de)}
.hero-photo-right{left:500px;top:0;width:351px;height:222px;background:linear-gradient(135deg,#f6f7f8,#d6dde3)}
.pill{width:96px;height:34px;border-radius:17px;color:#fff;font-weight:700;font-size:16px;display:flex;align-items:center;justify-content:center;box-shadow:0 2px 4px rgba(0,0,0,.15)}
.pill--daily{left:400px;top:26px;background:var(--green)}
.pill--traffic{left:400px;top:76px;background:var(--teal)}
.pill--sport{left:400px;top:126px;background:var(--orange)}

.director-photo{left:24px;top:372px;width:300px;height:236px;background:linear-gradient(180deg,#dfe8ec,#b9c7cf)}
.greeting{left:330px;top:378px;width:300px}
.greeting h2{font-size:24px;font-weight:900;color:var(--teal);margin-bottom:8px;letter-spacing:.02em}
.greeting p{font-size:11.5px;line-height:1.65;color:var(--ink)}
.greeting .sign{margin-top:6px;font-size:11px;color:var(--muted)}
.body-figure{left:640px;top:400px;width:195px;height:200px;border-radius:8px;background:radial-gradient(ellipse at center,#cfe4f2,#f2f8fc 70%)}

.band{left:0;right:0;height:10px;background:linear-gradient(90deg,var(--green),var(--teal))}
.band--mid{top:616px}
.band--foot{top:1186px;height:14px}

.section-head{height:30px;background:var(--green);color:#fff;font-weight:700;font-size:17px;display:flex;align-items:center;padding-left:14px;letter-spacing:.1em;border-radius:3px}
.hours-head{left:24px;top:640px;width:390px}
.hours{left:24px;top:678px;width:390px;border-collapse:collapse;font-size:14px}
.hours th,.hours td{border-bottom:1px solid #bcd;height:36px;text-align:center}
.hours th{font-weight:700}
.hours td.time{text-align:left;font-weight:700;padding-left:4px;white-space:nowrap}
.mark{display:inline-block;width:16px;height:16px;border-radius:50%;border:2px solid var(--teal)}
.dash{color:var(--muted)}
.hours-note{left:24px;top:792px;width:390px;font-size:10.5px;line-height:1.6;color:var(--muted)}

.detail-head{left:432px;top:640px;width:395px;background:var(--teal)}
.detail-head span{font-size:14px;margin-left:18px}
.details{left:432px;top:680px;width:395px}
.detail-row{display:flex;align-items:center;border-bottom:1px dotted #9bb;height:34px}
.detail-row .label{width:72px;font-size:14px;color:var(--teal-dark);font-weight:500}
.detail-row .value{font-size:14px}
.detail-row .value.big{font-size:20px;font-weight:900;color:var(--pink)}
.detail-row .value.small{font-size:12px;line-height:1.3}
.facebook{left:432px;top:860px;font-size:14px;color:var(--teal-dark)}

.flow-head{left:24px;top:890px;width:530px}
.flow{left:24px;top:930px;width:530px;display:flex;align-items:center;gap:6px}
.step{height:44px;padding:0 12px;border-radius:6px;color:#fff;font-weight:700;font-size:14px;display:flex;align-items:center;justify-content:center;text-align:center;line-height:1.2}
.step--1{background:var(--pink)}
.step--2{background:var(--teal)}
.step--3{background:var(--orange)}
.step--4{background:var(--pink);padding:0 20px}
.arrow{width:14px;height:14px}
.notes{left:24px;top:994px;width:540px}
.notes li{list-style:none;font-size:14.5px;font-weight:700;color:var(--teal-dark);margin-bottom:4px}
.notes li.sub{font-size:11px;font-weight:400;color:var(--ink);padding-left:14px;margin-bottom:2px}
.search{left:24px;top:1130px;font-size:17px;font-weight:900;color:var(--orange)}
.map{left:580px;top:890px;width:248px;height:230px;border:1px solid #ccd;background:linear-gradient(135deg,#f4f5ef,#e2e8dc)}
.url{left:580px;top:1134px;width:248px;text-align:center;font-size:13px;font-weight:700;color:var(--teal-dark)}
</style>
</head>
<body>
<div class="flyer">
  <div class="abs tagline">痛みを癒し　人を助ける</div>
  <h1 class="abs clinic-name">鈴風台接骨院</h1>
  <div class="abs title-rule"></div>

  <section class="abs hero">
    <div class="abs hero-photo-left" role="img" aria-label="施術の様子の写真"></div>
    <div class="abs hero-photo-right" role="img" aria-label="治療機器の写真"></div>
    <div class="abs pill pill--daily">日常生活</div>
    <div class="abs pill pill--traffic">交通事故</div>
    <div class="abs pill pill--sport">スポーツ</div>
  </section>

  <div class="abs director-photo" role="img" aria-label="院長の写真"></div>
  <section class="abs greeting">
    <h2>痛みで困っていませんか？</h2>
    <p>こんにちは。<br>鈴風台接骨院の院長の佐野和也です。<br>腰痛や肩こり、スポーツのケガや交通事故の痛みなど、日常のさまざまなお悩みに丁寧に向き合います。一人ひとりの症状に合わせた施術で、早期の回復を目指します。どうぞお気軽にご相談ください。</p>
    <p class="sign">皆様一同、お来院お待ちしております。</p>
  </section>
  <div class="abs body-figure" role="img" aria-label="人体と痛む部位の図"></div>

  <div class="abs band band--mid"></div>

  <div class="abs section-head hours-head">受付時間</div>
  <table class="abs hours">
    <tr><th></th><th>月</th><th>火</th><th>水</th><th>木</th><th>金</th><th>土</th></tr>
    <tr><td class="time">AM8：30～PM12：30</td><td><span class="mark"></span></td><td><span class="mark"></span></td><td><span class="mark"></span></td><td><span class="mark"></span></td><td><span class="mark"></span></td><td><span class="mark"></span></td></tr>
    <tr><td class="time">PM16：00～PM20：00</td><td><span class="mark"></span></td><td><span class="mark"></span></td><td><span class="mark"></span></td><td><span class="mark"></span></td><td><span class="mark"></span></td><td class="dash">―</td></tr>
  </table>
  <p class="abs hours-note">※土曜日午後・日曜・祝日は休診となります。<br>※ご予約の方を優先させていただきます。お気軽にお電話ください。</p>

  <div class="abs section-head detail-head">接骨院詳細<span>鈴風台接骨院</span></div>
  <div class="abs details">
    <div class="detail-row"><span class="label">address</span><span class="value small">名古屋市東区鈴風台2-8-1<br>ミドリビル1F</span></div>
    <div class="detail-row"><span class="label">tel</span><span class="value big">052-555-0184</span></div>
    <div class="detail-row"><span class="label">mobile</span><span class="value big">090-0000-5127</span></div>
    <div class="detail-row"><span class="label">mail</span><span class="value">info@suzukazedai-sk.example</span></div>
  </div>
  <div class="abs facebook">facebook　www.suzukazedai-sk.example</div>

  <div class="abs section-head flow-head">治療の流れ</div>
  <div class="abs flow">
    <div class="step step--1">問診・触診</div>
    <svg class="arrow" viewBox="0 0 14 14"><path d="M2 1 L12 7 L2 13 Z" fill="#1e98a8"/></svg>
    <div class="step step--2">理学検査</div>
    <svg class="arrow" viewBox="0 0 14 14"><path d="M2 1 L12 7 L2 13 Z" fill="#1e98a8"/></svg>
    <div class="step step--3">治療方針<br>の説明</div>
    <svg class="arrow" viewBox="0 0 14 14"><path d="M2 1 L12 7 L2 13 Z" fill="#1e98a8"/></svg>
    <div class="step step--4">ご説明</div>
  </div>
  <ul class="abs notes">
    <li>◆交通事故自賠責、労災、健康保険の取り扱いが可能です</li>
    <li>◆各種実費メニューもご用意しております</li>
    <li class="sub">・コンディショニング整体（30分）3,000円</li>
    <li class="sub">・スポーツテーピング（1部位）1,000円</li>
    <li class="sub">・骨盤矯正（40分）4,000円</li>
    <li class="sub">・低周波治療（15分）1,500円</li>
  </ul>
  <div class="abs search">『鈴風台接骨院で検索』</div>

  <div class="abs map" role="img" aria-label="接骨院周辺の地図"></div>
  <div class="abs url">www.suzukazedai-sk.example</div>

  <div class="abs band band--foot"></div>
</div>
</body>
</html>
```